Book Cover Design GML

Want a new book cover but want to use the same photo and change the sub name. This is for a brand called "Golden Maple Living". The book is called "Just Steps, Just Results"

This is for a 8.5 * 11 book size

We really want to brand the Golden Maple Living

I've attached a sample of an old book cover, the photo I want used and the golden maple living logo

Requirements
Must have
• Must have the logo,

must have the book title. "Just Steps, Just Results"

Must have "Featuring" The Golden Maple Living Fit Roll Card Game"

On the back put the logo and Golden Maple Living Nutrition

must have the authors name "Dana Holcomb" on the page

"The Prime Shape Roadmap"
Nice to have
• Golden Maple Living Presents:

the book title

```html
<!DOCTYPE html>
<html lang="en">
<head>
<meta charset="utf-8">
<title>Just Steps, Just Results — Book Cover</title>
<link rel="stylesheet" href="https://fonts.googleapis.com/css2?family=Bebas+Neue&family=Mulish:wght@400;500&family=Michroma&display=swap">
<style>
  :root {
    --stage: #dcdcdc;
    --cover: #000000;
    --ink: #ffffff;
    --mint: #8ee0cc;
    --mint-deep: #4fb9a4;
    --spine-edge: #1c1c1c;
  }
  * { margin: 0; padding: 0; box-sizing: border-box; }
  html, body { width: 1200px; height: 780px; overflow: hidden; }
  body { background: var(--stage); position: relative; font-family: "Mulish", sans-serif; color: var(--ink); }

  .spread {
    position: absolute; left: 60px; top: 60px; width: 1080px; height: 660px;
    background: var(--cover); box-shadow: 6px 8px 14px rgba(0,0,0,.35);
  }

  /* Back cover */
  .back { position: absolute; left: 0; top: 0; width: 510px; height: 660px; overflow: hidden; }
  .brand-mark {
    position: absolute; left: 195px; top: 70px; width: 120px; height: 120px;
    border: 6px solid var(--ink);
  }
  .brand-block { position: absolute; left: 0; width: 510px; top: 250px; text-align: center; }
  .brand-name { font-family: "Michroma", sans-serif; font-size: 19px; letter-spacing: 2px; }
  .brand-sub { font-family: "Mulish", sans-serif; font-size: 12px; letter-spacing: 7px; margin-top: 6px; }
  .brand-tag { font-family: "Mulish", sans-serif; font-size: 7px; letter-spacing: 2px; margin-top: 8px; }
  .blurb {
    position: absolute; left: 58px; top: 340px; width: 394px;
    font-family: "Bebas Neue", sans-serif; font-size: 15px; line-height: 20px; letter-spacing: 0;
  }
  .blurb-line { display: block; white-space: nowrap; text-align: justify; text-align-last: justify; }
  .blurb-line.last { text-align-last: left; }
  .blurb-short { top: 544px; width: 250px; }
  .blurb-short .blurb-line { text-align-last: left; }

  /* Spine */
  .spine {
    position: absolute; left: 510px; top: 0; width: 60px; height: 660px;
    border-left: 1px solid var(--spine-edge); border-right: 1px solid var(--spine-edge);
  }
  .spine-text {
    position: absolute; left: 50%; writing-mode: vertical-rl; transform: translateX(-50%) rotate(180deg);
    white-space: nowrap;
  }
  .spine-brand { top: 36px; font-family: "Michroma", sans-serif; font-size: 9px; letter-spacing: 1px; }
  .spine-title { top: 212px; font-family: "Bebas Neue", sans-serif; font-size: 34px; letter-spacing: .5px; }
  .spine-author { top: 504px; font-family: "Mulish", sans-serif; font-size: 16px; letter-spacing: 1px; }

  /* Front cover */
  .front { position: absolute; left: 570px; top: 0; width: 510px; height: 660px; overflow: hidden; }
  .cover-photo {
    position: absolute; left: 82px; top: 4px; width: 428px; height: 656px;
    background:
      radial-gradient(circle at 110px 330px, var(--mint-deep) 0, #2d6f63 90px, rgba(0,0,0,0) 150px),
      radial-gradient(ellipse at 300px 340px, #4a3226 0, #231a15 140px, rgba(0,0,0,0) 260px);
  }
  .series { position: absolute; left: 38px; top: 38px; font-size: 19px; letter-spacing: .5px; }
  .series-rule { position: absolute; left: 38px; top: 65px; width: 280px; height: 2px; background: var(--mint); }
  .game { position: absolute; left: 38px; top: 74px; line-height: 1; }
  .game-line { font-size: 19px; letter-spacing: .5px; }
  .game-accent { font-size: 29px; color: var(--mint); margin: 3px 0 4px; letter-spacing: .5px; }
  .title {
    position: absolute; left: 36px; top: 338px; width: 460px;
    font-family: "Bebas Neue", sans-serif; font-weight: 400; font-size: 100px; line-height: 96px; letter-spacing: 1px;
    white-space: nowrap;
  }
  .author { position: absolute; left: 38px; top: 576px; font-size: 25px; line-height: 30px; color: var(--mint); letter-spacing: 1px; }
</style>
</head>
<body>
  <section class="spread">
    <div class="back">
      <div class="brand-mark"></div>
      <div class="brand-block">
        <div class="brand-name">GOLDEN MAPLE</div>
        <div class="brand-sub">LIVING</div>
        <div class="brand-tag">NUTRITION</div>
      </div>
      <p class="blurb">
        <span class="blurb-line">Lorem ipsum dolor sit amet, consectetuer adipiscing elit, sed diam</span>
        <span class="blurb-line">nonummy nibh euismod tincidunt ut laoreet dolore magna aliquam erat</span>
        <span class="blurb-line">volutpat. Ut wisi enim ad minim veniam, quis nostrud exerci tation</span>
        <span class="blurb-line">ullamcorper suscipit lobortis nisl ut aliquip ex ea commodo consequat.</span>
        <span class="blurb-line">Duis autem vel eum iriure dolor in hendrerit in vulputate velit esse</span>
        <span class="blurb-line">molestie consequat, vel illum dolore eu feugiat nulla facilisis at vero</span>
        <span class="blurb-line">eros et accumsan et iusto odio dignissim qui blandit praesent luptatum</span>
        <span class="blurb-line last">zzril delenit augue duis dolore te feugait nulla facilisi.</span>
      </p>
      <p class="blurb blurb-short">
        <span class="blurb-line">Lorem ipsum dolor sit amet, consectetuer</span>
        <span class="blurb-line">adipiscing elit, sed diam nonummy nibh</span>
        <span class="blurb-line">euismod tincidunt ut laoreet dolore magna</span>
      </p>
    </div>

    <div class="spine">
      <div class="spine-text spine-brand">GOLDEN MAPLE LIVING</div>
      <div class="spine-text spine-title">JUST STEPS JUST RESULTS</div>
      <div class="spine-text spine-author">DANA HOLCOMB</div>
    </div>

    <div class="front">
      <div class="cover-photo" role="img" aria-label="Photo of the author in sportswear, standing with one arm resting on a mint exercise ball"></div>
      <div class="series">THE PRIME SHAPE ROADMAP</div>
      <div class="series-rule"></div>
      <div class="game">
        <div class="game-line">THE GOLDEN MAPLE LIVING</div>
        <div class="game-accent">FIT ROLL</div>
        <div class="game-line">CARD GAME</div>
      </div>
      <h1 class="title">JUST STEPS<br>JUST RESULTS</h1>
      <div class="author">DANA HOLCOMB</div>
    </div>
  </section>
</body>
</html>
```